DJQuorbel.com

A clean-looking fun website.

MAP*

top* Video. (To host party footage and also to host live streams as they happen.

Tabs - Events, Livestream, Mixes, Playlists, Sign up, Photos, Bio, Shop

Links to Instagram, Facebook and Twitter, YouTube & Twitch

sign up sheet to take contact details for future promo.

References
http://www.djbrisklomb.com/
http://www.kasperdrune.com/
https://torvinmesk.com/
https://www.djvormaniofficial.com/
https://lenfrask.com/
https://www.samtivvey.com/den/

I hope this helps.

```html
<!DOCTYPE html>
<html lang="en">
<head>
<meta charset="utf-8">
<title>DJQuorbel</title>
<link href="https://fonts.googleapis.com/css2?family=Oswald:wght@500;600;700&family=Open+Sans:wght@400;600;700&display=swap" rel="stylesheet">
<style>
:root{
  --accent:#e63f1d;
  --accent-dark:#b82c10;
  --ink:#111111;
  --dark:#141414;
  --dark-2:#1d1d1d;
  --light:#f1f1f1;
  --white:#ffffff;
  --muted:#8a8a8a;
  --text:#333333;
}
*{margin:0;padding:0;box-sizing:border-box}
html,body{width:1200px;height:4376px;overflow:hidden}
body{font-family:"Open Sans",Arial,sans-serif;color:var(--text);background:var(--white);position:relative}
.section-title{font-family:"Oswald",Impact,sans-serif;font-weight:700;text-transform:uppercase;font-size:34px;text-align:center;letter-spacing:1px}
.btn{display:inline-block;font-family:"Open Sans",Arial,sans-serif;font-weight:700;font-size:15px;text-transform:uppercase;padding:12px 26px;border-radius:4px;white-space:nowrap}
.btn-accent{background:var(--accent);color:var(--white)}
.btn-light{background:var(--white);color:var(--ink)}

/* header */
.site-header{position:absolute;top:0;left:0;width:1200px;height:80px;background:var(--white);display:flex;align-items:center;padding:0 128px}
.brand{font-family:"Oswald",Impact,sans-serif;font-weight:700;font-size:34px;color:var(--ink);letter-spacing:1px;display:flex;align-items:center;gap:10px}
.brand-dot{width:14px;height:14px;background:var(--ink);border-radius:50%}
.main-nav{display:flex;gap:30px;margin-left:60px}
.main-nav a{font-size:14px;font-weight:600;color:var(--ink);text-decoration:none;text-transform:uppercase;padding-bottom:6px}
.main-nav a.active{border-bottom:2px solid var(--ink)}

/* hero */
.hero{position:absolute;top:80px;left:0;width:1200px;height:632px;background:radial-gradient(ellipse at 45% 25%,#f08a3a 0%,#b4471a 25%,#4a1a0c 55%,#120705 85%)}
.hero-media{position:absolute;inset:0}
.play-btn{position:absolute;left:558px;top:288px;width:68px;height:68px;border-radius:50%;background:var(--white);display:flex;align-items:center;justify-content:center}
.hero-title{position:absolute;left:790px;top:290px;color:var(--white);font-family:"Oswald",Impact,sans-serif;font-weight:700;text-transform:uppercase;line-height:1.05}
.hero-title .small{font-size:48px;display:block}
.hero-title .big{font-size:62px;display:block}

/* about */
.about{position:absolute;top:712px;left:0;width:1200px;height:608px;background:linear-gradient(90deg,#2a2a2a 0%,#3a3a3a 30%,#181818 55%,#0c0c0c 100%)}
.about-photo{position:absolute;left:0;top:0;width:620px;height:608px;background:linear-gradient(180deg,#4a4a4a 0%,#262626 60%,#101010 100%)}
.about-body{position:absolute;left:672px;top:80px;width:470px;color:var(--white)}
.about-body h2{font-family:"Oswald",Impact,sans-serif;font-size:38px;font-weight:700;text-transform:uppercase;margin-bottom:18px}
.about-body p{font-size:16px;line-height:1.55;margin-bottom:26px}

/* mixes */
.mixes{position:absolute;top:1320px;left:0;width:1200px;height:680px;background:linear-gradient(180deg,#161616,#0d0d0d)}
.mixes .section-title{color:var(--white);margin-top:60px}
.mix-grid{position:absolute;left:128px;top:144px;width:944px;display:grid;grid-template-columns:460px 460px;gap:24px}
.mix-card{height:176px;background:var(--white);display:flex}
.mix-photo{width:196px;height:176px;flex:none}
.mix-info{flex:1;padding:18px 16px 0}
.mix-top{display:flex;gap:12px;align-items:flex-start}
.mix-icon{flex:none;width:28px;height:28px;border-radius:50%;background:var(--accent);display:flex;align-items:center;justify-content:center}
.mix-name{font-size:11px;font-weight:700;text-transform:uppercase;color:var(--ink);line-height:1.4}
.mix-meta{display:flex;gap:18px;font-size:11px;color:var(--muted);margin:12px 0 8px 40px}
.wave{height:64px;background:repeating-linear-gradient(90deg,var(--accent) 0 3px,transparent 3px 6px);-webkit-mask:linear-gradient(180deg,transparent 0%,#000 30%,#000 70%,transparent 100%);mask:linear-gradient(180deg,transparent 0%,#000 30%,#000 70%,transparent 100%)}
.mixes .btn{position:absolute;left:532px;top:590px}

/* events */
.events{position:absolute;top:2000px;left:0;width:1200px;height:628px;background:var(--light)}
.events .section-title{color:var(--ink);margin-top:60px}
.event-slide{position:absolute;left:128px;top:140px;width:944px;height:420px;background:var(--dark-2);display:flex}
.event-photo{width:296px;height:420px;flex:none;background:linear-gradient(160deg,#8a5ec8 0%,#5a3e8a 35%,#2e2338 70%,#1a1420 100%)}
.event-body{padding:60px 40px 0;color:var(--white)}
.event-date{display:inline-block;font-size:13px;background:#333;padding:4px 10px;margin-bottom:20px}
.event-body h3{font-family:"Oswald",Impact,sans-serif;font-size:24px;font-weight:600;text-transform:uppercase;line-height:1.2;margin-bottom:14px}
.event-body p{font-size:14px;line-height:1.5;margin-bottom:20px;color:#ddd}
.event-body .btn{font-size:12px;padding:9px 18px}
.slider-arrow{position:absolute;width:38px;height:38px;border-radius:50%;background:var(--ink);display:flex;align-items:center;justify-content:center}

/* shop */
.shop{position:absolute;top:2628px;left:0;width:1200px;height:512px;background:var(--white)}
.shop .section-title{color:var(--ink);margin-top:62px}
.product-row{position:absolute;left:128px;top:144px;display:flex;gap:20px}
.product{width:220px;height:300px;border:1px solid #cfcfcf;background:var(--white);text-align:center}
.product-img{width:160px;height:180px;margin:20px auto 18px;border-radius:6px}
.product-name{font-size:11px;font-weight:700;text-transform:uppercase;color:var(--ink)}
.product-price{font-size:18px;font-weight:700;color:var(--accent);margin-top:6px}
.shop-arrow{position:absolute;top:286px}

/* gallery */
.gallery{position:absolute;top:3140px;left:0;width:1200px;height:860px;background:#f3f3f3}
.gallery .section-title{color:var(--ink);margin-top:60px}
.gallery-grid{position:absolute;left:128px;top:120px;display:grid;grid-template-columns:300px 300px 304px;gap:20px}
.gallery-item{height:290px}
.gallery .btn{position:absolute;left:528px;top:770px}

/* footer */
.site-footer{position:absolute;top:4000px;left:0;width:1200px;height:376px;background:#050505;color:var(--white)}
.footer-brand{position:absolute;left:128px;top:80px;font-family:"Oswald",Impact,sans-serif;font-size:48px;font-weight:700;letter-spacing:1px;display:flex;align-items:center;gap:12px}
.footer-brand .brand-dot{background:var(--white);width:18px;height:18px}
.footer-col{position:absolute;top:44px}
.footer-col h4{font-size:13px;font-weight:700;text-transform:uppercase;margin-bottom:14px}
.footer-menu li{list-style:none;font-size:12px;line-height:1.55;text-transform:uppercase;color:#ddd}
.contact-item{display:flex;gap:12px;align-items:flex-start;margin-bottom:14px;font-size:12px;line-height:1.45;color:#ddd}
.contact-icon{flex:none;width:26px;height:26px;border-radius:50%;background:var(--white);display:flex;align-items:center;justify-content:center}
.social{display:flex;gap:8px}
.social span{width:24px;height:24px;border-radius:50%;background:var(--accent)}
.copyright{position:absolute;left:0;width:1200px;top:340px;text-align:center;font-size:11px;color:#aaa}
</style>
</head>
<body>

<header class="site-header">
  <div class="brand"><span class="brand-dot"></span>QUORBEL</div>
  <nav class="main-nav">
    <a class="active">Home</a><a>Events</a><a>Livestream</a><a>Mixes</a><a>Playlists</a><a>Sign Up</a><a>Photos</a><a>Bio</a><a>Shop</a>
  </nav>
</header>

<section class="hero">
  <div class="hero-media" role="img" aria-label="Party footage video: DJ performing with a microphone behind the decks under orange stage lights"></div>
  <div class="play-btn">
    <svg width="28" height="28" viewBox="0 0 24 24"><path d="M8 5l12 7-12 7z" fill="#111"/></svg>
  </div>
  <h1 class="hero-title"><span class="small">Welcome to</span><span class="big">DJQuorbel</span></h1>
</section>

<section class="about">
  <div class="about-photo" role="img" aria-label="Black and white photo of the DJ playing a set at the decks"></div>
  <div class="about-body">
    <h2>About</h2>
    <p>On the other hand, we denounce with righteous indignation and dislike men who are so beguiled and demoralized by the charms of pleasure of the moment, so blinded by desire, that they cannot foresee the pain and trouble that are bound to ensue; and equal blame belongs to those who fail in their duty through weakness of will, which is the same as saying through shrinking from toil and pain. These cases are perfectly simple and easy to distinguish.</p>
    <span class="btn btn-light">Read More</span>
  </div>
</section>

<section class="mixes">
  <h2 class="section-title">Mixes</h2>
  <div class="mix-grid">
    <article class="mix-card">
      <div class="mix-photo" role="img" aria-label="DJ at the decks under warm stage lights" style="background:linear-gradient(160deg,#c4703a,#5a2a18)"></div>
      <div class="mix-info">
        <div class="mix-top"><span class="mix-icon"><svg width="12" height="12" viewBox="0 0 24 24"><path d="M7 4l13 8-13 8z" fill="#fff"/></svg></span>
        <div class="mix-name">At vero eos et accusamus et iusto odio dignissim</div></div>
        <div class="mix-meta"><span>08.03.21</span><span>MAR 2021</span></div>
        <div class="wave"></div>
      </div>
    </article>
    <article class="mix-card">
      <div class="mix-photo" role="img" aria-label="DJ booth lit in deep red" style="background:linear-gradient(160deg,#d2261a,#4a0c08)"></div>
      <div class="mix-info">
        <div class="mix-top"><span class="mix-icon"><svg width="12" height="12" viewBox="0 0 24 24"><path d="M7 4l13 8-13 8z" fill="#fff"/></svg></span>
        <div class="mix-name">At vero eos et accusamus et iusto odio dignissim</div></div>
        <div class="mix-meta"><span>08.03.21</span><span>MAR 2021</span></div>
        <div class="wave"></div>
      </div>
    </article>
    <article class="mix-card">
      <div class="mix-photo" role="img" aria-label="DJ performing with a microphone on stage" style="background:linear-gradient(160deg,#b8602e,#3a1a10)"></div>
      <div class="mix-info">
        <div class="mix-top"><span class="mix-icon"><svg width="12" height="12" viewBox="0 0 24 24"><path d="M7 4l13 8-13 8z" fill="#fff"/></svg></span>
        <div class="mix-name">At vero eos et accusamus et iusto odio dignissim</div></div>
        <div class="mix-meta"><span>08.03.21</span><span>MAR 2021</span></div>
        <div class="wave"></div>
      </div>
    </article>
    <article class="mix-card">
      <div class="mix-photo" role="img" aria-label="Crowd at a concert with bright stage lights" style="background:linear-gradient(160deg,#e8a040,#3a1c10)"></div>
      <div class="mix-info">
        <div class="mix-top"><span class="mix-icon"><svg width="12" height="12" viewBox="0 0 24 24"><path d="M7 4l13 8-13 8z" fill="#fff"/></svg></span>
        <div class="mix-name">At vero eos et accusamus et iusto odio dignissim</div></div>
        <div class="mix-meta"><span>08.03.21</span><span>MAR 2021</span></div>
        <div class="wave"></div>
      </div>
    </article>
  </div>
  <span class="btn btn-accent">View All Mixes</span>
</section>

<section class="events">
  <h2 class="section-title">Latest Events</h2>
  <div class="event-slide">
    <div class="event-photo" role="img" aria-label="Group of friends posing at a party under purple lights"></div>
    <div class="event-body">
      <span class="event-date">15 Aug, 2021</span>
      <h3>On the other hand, we denounce with righte ous indignation</h3>
      <p>On the other hand, we denounce with righteous indignation and dislike men who are so beguiled and demoralized by the charms of pleasure of the moment, so blinded by desire.</p>
      <span class="btn btn-accent">Read More</span>
    </div>
  </div>
  <span class="slider-arrow" style="left:54px;top:341px"><svg width="14" height="14" viewBox="0 0 24 24"><path d="M15 4l-8 8 8 8" stroke="#fff" stroke-width="3" fill="none"/></svg></span>
  <span class="slider-arrow" style="left:1106px;top:341px"><svg width="14" height="14" viewBox="0 0 24 24"><path d="M9 4l8 8-8 8" stroke="#fff" stroke-width="3" fill="none"/></svg></span>
</section>

<section class="shop">
  <h2 class="section-title">Shop</h2>
  <div class="product-row">
    <div class="product"><div class="product-img" role="img" aria-label="Black T-shirt with colourful print" style="background:#1a1a1a"></div><div class="product-name">At vero eos et accusamus</div><div class="product-price">$15.00</div></div>
    <div class="product"><div class="product-img" role="img" aria-label="Black T-shirt with white print" style="background:#1a1a1a"></div><div class="product-name">At vero eos et accusamus</div><div class="product-price">$15.00</div></div>
    <div class="product"><div class="product-img" role="img" aria-label="Black T-shirt with small chest print" style="background:#1a1a1a"></div><div class="product-name">At vero eos et accusamus</div><div class="product-price">$15.00</div></div>
    <div class="product"><div class="product-img" role="img" aria-label="Beige T-shirt with dark print" style="background:#c9b28e"></div><div class="product-name">At vero eos et accusamus</div><div class="product-price">$15.00</div></div>
  </div>
  <svg class="shop-arrow" style="left:72px" width="16" height="20" viewBox="0 0 16 20"><path d="M12 2L4 10l8 8" stroke="#333" stroke-width="2.5" fill="none"/></svg>
  <svg class="shop-arrow" style="left:1110px" width="16" height="20" viewBox="0 0 16 20"><path d="M4 2l8 8-8 8" stroke="#333" stroke-width="2.5" fill="none"/></svg>
</section>

<section class="gallery">
  <h2 class="section-title">Gallery</h2>
  <div class="gallery-grid">
    <div class="gallery-item" role="img" aria-label="DJ singing into a microphone in orange light" style="background:linear-gradient(160deg,#d07a3a,#2a1208)"></div>
    <div class="gallery-item" role="img" aria-label="DJ posing behind the decks" style="background:linear-gradient(160deg,#7a6aa0,#2a2030)"></div>
    <div class="gallery-item" role="img" aria-label="DJ booth in red lighting" style="background:linear-gradient(160deg,#e0301c,#3a0806)"></div>
    <div class="gallery-item" role="img" aria-label="Crowd with hands raised under purple lights" style="background:linear-gradient(160deg,#8a4ac8,#1a0c2a)"></div>
    <div class="gallery-item" role="img" aria-label="Concert crowd facing a bright stage" style="background:linear-gradient(160deg,#e8d0b0,#3a2a20)"></div>
    <div class="gallery-item" role="img" aria-label="Stage lights over a packed dance floor" style="background:linear-gradient(160deg,#d84020,#1a0604)"></div>
  </div>
  <span class="btn btn-accent">View All Photos</span>
</section>

<footer class="site-footer">
  <div class="footer-brand"><span class="brand-dot"></span>QUORBEL</div>
  <div class="footer-col" style="left:460px">
    <h4>Menu</h4>
    <ul class="footer-menu"><li>Home</li><li>Events</li><li>Livestream</li><li>Mixes</li><li>Playlists</li><li>Sign Up</li><li>Photos</li><li>Bio</li><li>Shop</li></ul>
  </div>
  <div class="footer-col" style="left:648px">
    <h4>Contact Us</h4>
    <div class="contact-item"><span class="contact-icon"><svg width="12" height="12" viewBox="0 0 24 24"><path d="M12 2a7 7 0 0 0-7 7c0 5 7 13 7 13s7-8 7-13a7 7 0 0 0-7-7zm0 9.5A2.5 2.5 0 1 1 12 6.5a2.5 2.5 0 0 1 0 5z" fill="#111"/></svg></span><span>4820 Larkmoor Street<br>Delton, NV 89102</span></div>
    <div class="contact-item"><span class="contact-icon"><svg width="12" height="12" viewBox="0 0 24 24"><path d="M6.6 10.8a15 15 0 0 0 6.6 6.6l2.2-2.2a1 1 0 0 1 1-.25 11 11 0 0 0 3.6.6 1 1 0 0 1 1 1V20a1 1 0 0 1-1 1A17 17 0 0 1 3 4a1 1 0 0 1 1-1h3.5a1 1 0 0 1 1 1 11 11 0 0 0 .6 3.6 1 1 0 0 1-.25 1z" fill="#111"/></svg></span><span>Call Us<br>555-0148-2290</span></div>
    <div class="contact-item"><span class="contact-icon"><svg width="12" height="12" viewBox="0 0 24 24"><path d="M3 5h18v14H3z" fill="#111"/><path d="M3 5l9 7 9-7" stroke="#fff" stroke-width="1.6" fill="none"/></svg></span><span>E-mail Us<br>info@djquorbel.com</span></div>
  </div>
  <div class="footer-col" style="left:888px">
    <h4>Follow Us</h4>
    <div class="social" role="list" aria-label="Social media links"><span role="listitem"></span><span role="listitem"></span><span role="listitem"></span><span role="listitem"></span><span role="listitem"></span></div>
  </div>
  <p class="copyright">Copyright © 2024 DJQuorbel. All Rights Reserved.</p>
</footer>

</body>
</html>
```